Business Improvement Consultancy needs web design

I need a web design for my company, that offers support to manufacturing and distribution businesses.

We have worked with a range of organisations to help them get more out of their operational processes and supply chains.

With full end to end supply chain knowledge we help them identify waste in their supply chains that often get overlooked.

We support through a number of offerings

Developing an end to end supply chain strategy

Applying Lean to support the strategy

Interim support network to deliver quick wins and rapid cost improvement

Project Management

Interactive training tools for delivering supply chain best practice.

I have the logos done already, so it is more about look and feel, and the colour schemes etc giving a professional feel.

Also have the web domains www.tessarongroup.co, www.tessarongroup.co.uk & www.tessarongroup.eu, using Nubo beginner package

Target Market(s)

Manufacturing and distribution businesses, potentially other consultancies looking for collaboration

Industry/Entity Type

Business

Requirements
Must have
• Some pictures on related to performance improvement, bar charts showing productivity growth / increase.

Should have the facebook twitter and linkedin logos to share the website

```html
<!DOCTYPE html>
<html lang="en">
<head>
<meta charset="utf-8">
<title>Tessaron Group – About Us</title>
<link href="https://fonts.googleapis.com/css2?family=PT+Sans:wght@400;700&display=swap" rel="stylesheet">
<style>
:root{
  --navy:#29286c;
  --navy-light:#3c3c8a;
  --ink:#222;
  --body:#4a4a4a;
  --grey-bar:#a9a9a9;
  --nav-bg:#e6e6e6;
  --nav-text:#8a8a8a;
  --rule:#d0d0d0;
  --white:#fff;
}
*{margin:0;padding:0;box-sizing:border-box}
html,body{width:1200px;height:970px;overflow:hidden;background:var(--white)}
body{position:relative;font-family:"PT Sans",Arial,sans-serif;color:var(--body)}
.abs{position:absolute}
.top-bar{left:0;top:0;width:1200px;height:7px;background:var(--grey-bar)}

.brand{left:145px;top:48px;display:flex;align-items:center;gap:14px}
.brand-dot{width:40px;height:40px;border-radius:50%;background:var(--navy)}
.brand-name{font-size:28px;color:var(--navy);font-weight:400}

.social{left:848px;top:47px;display:flex;gap:16px}
.social-btn{width:57px;height:57px;border-radius:9px;background:linear-gradient(#5a5aa0,var(--navy))}
.social-btn.round{border-radius:50%;background:linear-gradient(#e4e4ee,#b9b9cf)}

.main-nav{left:135px;top:141px;width:946px;height:49px;background:linear-gradient(#efefef,#dedede);display:flex;align-items:center}
.nav-item{position:relative;height:49px;display:flex;align-items:center;justify-content:center;font-size:17px;font-weight:700;color:var(--nav-text)}
.nav-item.sep::before{content:"";position:absolute;left:0;top:9px;height:31px;width:1px;background:#c4c4c4}
.nav-item.active{height:56px;align-self:flex-start;background:linear-gradient(var(--navy-light),var(--navy));color:var(--white);padding-bottom:7px}
.nav-item.active::after{content:"";position:absolute;bottom:-1px;left:50%;margin-left:-6px;border:6px solid transparent;border-bottom-color:var(--white)}

.hero{left:135px;top:218px;width:946px;height:238px;border:1px solid var(--rule);background:linear-gradient(90deg,#f4f7fb 0%,#e8eef5 55%,#dfe6ee 100%)}
.hero-photo{position:absolute;right:0;top:0;width:440px;height:236px;background:linear-gradient(100deg,#e9eef4 0%,#c7ccd3 35%,#8b8f98 60%,#c9ced6 100%)}
.hero-panel{position:absolute;left:7px;top:7px;width:500px;height:223px;border:3px solid #55528f;background:rgba(255,255,255,.82);padding:0 10px 0 14px}
.hero-title{display:flex;align-items:center;gap:12px;margin:38px 0 0 0;font-size:29px;font-weight:700;color:var(--navy)}
.hero-title .dot{width:22px;height:22px;border-radius:50%;background:var(--navy)}
.hero-panel p{font-size:14px;line-height:17.5px;color:#111;font-weight:700;margin-top:35px;letter-spacing:-.2px}
.hero-panel p + p{margin-top:17px}

.section-title{font-size:25px;font-weight:700;color:var(--navy);text-transform:uppercase;letter-spacing:-.3px}
.about-title{left:135px;top:484px}
.about-text{left:135px;top:530px;width:612px;font-size:13.5px;line-height:16.4px}
.about-text p{margin-bottom:12px}

.offering{top:704px;width:204px;height:154px;border:1px solid #9a9a9a;background:linear-gradient(160deg,#dfe4ee,#8d97ad);overflow:hidden}
.offering.chart{background:linear-gradient(160deg,#ffffff,#c9d7f1 60%,#5a7fd0)}
.offering.team{background:linear-gradient(160deg,#dde3ee,#6c7590 60%,#2e3550)}
.offering-caption{position:absolute;left:0;bottom:0;width:100%;height:36px;background:rgba(235,235,240,.82);padding:1px 7px;font-size:14px;line-height:17px;color:#111;font-weight:700}
.o1{left:133px}.o2{left:341px}.o3{left:550px}
.o2 .offering-caption,.o3 .offering-caption{padding-left:9px;padding-right:30px}

.divider{left:763px;top:484px;width:1px;height:377px;background:var(--rule)}

.news-title{left:791px;top:484px}
.news-list{left:791px;top:531px;width:300px}
.news-item{display:flex;gap:17px;height:86px}
.news-date{position:relative;flex:none;width:68px;height:68px;background:linear-gradient(#e2e2e2,#8e8e8e);box-shadow:0 1px 2px rgba(0,0,0,.3);text-align:center;font-size:20px;line-height:23px;color:#1c1c1c;padding-top:18px}
.news-date::before{content:"";position:absolute;left:31px;top:4px;width:7px;height:7px;border-radius:50%;background:#fff;border:1px solid #777}
.news-text{width:210px}
.news-head{font-size:13.5px;font-weight:700;color:var(--navy);margin-top:-3px}
.news-body{font-size:13px;line-height:16.4px;color:var(--body);margin-top:6px}

.site-footer{left:0;top:883px;width:1200px;height:87px;background:var(--grey-bar);border-top:2px solid #909090;text-align:center;font-size:13.5px;color:#111;padding-top:15px;line-height:22px}
</style>
</head>
<body>
<div class="abs top-bar"></div>

<header>
  <div class="abs brand"><span class="brand-dot"></span><span class="brand-name">Tessaron Group</span></div>
  <div class="abs social" aria-label="Share links">
    <span class="social-btn" role="img" aria-label="Share on professional network"></span>
    <span class="social-btn" role="img" aria-label="Share on social network"></span>
    <span class="social-btn round" role="img" aria-label="Share on microblog"></span>
  </div>
  <nav class="abs main-nav">
    <span class="nav-item" style="width:150px">Home</span>
    <span class="nav-item active" style="width:156px">About Us</span>
    <span class="nav-item" style="width:142px">Consultancy</span>
    <span class="nav-item sep" style="width:120px">Interim</span>
    <span class="nav-item sep" style="width:221px">Project Management</span>
    <span class="nav-item sep" style="width:157px">Contact Us</span>
  </nav>
</header>

<section class="abs hero">
  <div class="hero-photo" role="img" aria-label="Photo of a smiling businessman in a meeting room"></div>
  <div class="hero-panel">
    <h1 class="hero-title"><span class="dot"></span>Tessaron - to improve, to enhance</h1>
    <p>Welcome to Tessaron Group. We have worked with a range of organisations to help them get more out of their operational processes and supply chains.</p>
    <p>With full end to end supply chain knowledge we can help you identify waste in your supply chains that often get overlooked.</p>
  </div>
</section>

<h2 class="abs section-title about-title">About Us</h2>
<div class="abs about-text">
  <p>Lorem Ipsum is simply dummy text of the printing and typesetting industry. Lorem Ipsum has been the industry's standard dummy text ever since the 1500s, when an unknown printer took a galley of type and scrambled it to make a type specimen book. It has survived not only five centuries, but also the leap into electronic typesetting, remaining essentially unchanged.</p>
  <p>It was popularised in the 1960s with the release of Typeline sheets containing Lorem Ipsum passages, and more recently with desktop publishing software like Quill Layout including versions of Lorem Ipsum.</p>
  <p>It has survived not only five centuries, but also the leap into electronic typesetting, remaining essentially unchanged.</p>
</div>

<div class="abs offering o1" role="img" aria-label="Photo of business people shaking hands"><div class="offering-caption">We support through a number of offerings</div></div>
<div class="abs offering chart o2" role="img" aria-label="Illustration of a rising blue bar chart"><div class="offering-caption">Developing an end to end supply chain strategy</div></div>
<div class="abs offering team o3" role="img" aria-label="Photo of a business team seated in a row"><div class="offering-caption">Applying Lean to support the strategy</div></div>

<div class="abs divider"></div>

<h2 class="abs section-title news-title">Latest News</h2>
<div class="abs news-list">
  <article class="news-item"><div class="news-date">16<br>SEPT</div><div class="news-text"><div class="news-head">Lorem Ipsum is simply</div><div class="news-body">Lorem Ipsum is simply dummy text of the printing and typesetting industry. Lorem Ipsum has ...</div></div></article>
  <article class="news-item"><div class="news-date">16<br>SEPT</div><div class="news-text"><div class="news-head">Lorem Ipsum is simply</div><div class="news-body">Lorem Ipsum is simply dummy text of the printing and typesetting industry. Lorem Ipsum has ...</div></div></article>
  <article class="news-item"><div class="news-date">16<br>SEPT</div><div class="news-text"><div class="news-head">Lorem Ipsum is simply</div><div class="news-body">Lorem Ipsum is simply dummy text of the printing and typesetting industry. Lorem Ipsum has ...</div></div></article>
  <article class="news-item"><div class="news-date">16<br>SEPT</div><div class="news-text"><div class="news-head">Lorem Ipsum is simply</div><div class="news-body">Lorem Ipsum is simply dummy text of the printing and typesetting industry. Lorem Ipsum has ...</div></div></article>
</div>

<footer class="abs site-footer">
  <div>Home &nbsp;|&nbsp; About Us &nbsp;|&nbsp; Consultancy &nbsp;|&nbsp; Interim &nbsp;|&nbsp; Project Management &nbsp;|&nbsp; Contact Us</div>
  <div>Tessaron Group, PO Box 2048 Fernvale, Europe. E-mail: hello@tessarongroup.eu</div>
  <div>Copyright © 2011 all rights reserved, privacy policy.</div>
</footer>
</body>
</html>
```